Velumin clinic business card - double sided for young clinic

I require business cards for my aesthetic clinic specialising in the below treatments. I would like the cards to be modern as my clinic base are young 22-35 years old. I require my logo on it and would like the edges to be rounded.

I have an aesthetic clinic specialising in :
Velumin
Lip Enhancement
Chemical Peels
Facial Fillers
Non Surgical Face Lift

I would the cards to have the following information on them:
My logo - (in grey/silver)
address
Phone number
services

Colours :
White/grey/silver and red

a nice image on there, perhaps a set of lips as this is a main service i deliver

Company Name: HFA Address: 52 Harwell Lane, 4 Brimfold High Street, TN7 4QW Phone: 0207 948 2176 Website: www.helenfosburyaesthetics-example.co.uk

Target Market(s)

clinics 22-45 years old mainly female

Industry/Entity Type

Business

Contact Information for Business Card

as above

Requirements
Must have
• logo
• Address
• Email
• Phone number
• Services i offer
Nice to have
• images

```html
<!DOCTYPE html>
<html lang="en">
<head>
<meta charset="utf-8">
<title>HFA Business Card – Front and Back</title>
<link rel="stylesheet" href="https://fonts.googleapis.com/css2?family=Open+Sans:wght@400;600;700&family=Crimson+Text:wght@400;600&display=swap">
<style>
  :root {
    --backdrop-top: #7a7a7a;
    --backdrop-bottom: #454545;
    --card-charcoal: #231f20;
    --card-black: #000000;
    --divider-white: #ffffff;
    --logo-silver: #d9dcdb;
    --name-grey: #c9c9c9;
    --text-white: #ffffff;
  }
  * { margin: 0; padding: 0; box-sizing: border-box; }
  html, body { width: 1200px; height: 900px; overflow: hidden; }
  body {
    background: linear-gradient(to bottom, var(--backdrop-top), var(--backdrop-bottom));
    font-family: "Open Sans", Arial, sans-serif;
    position: relative;
  }
  .card {
    position: absolute;
    top: 306px;
    width: 440px;
    height: 271px;
    border-radius: 10px;
    overflow: hidden;
    background: var(--card-charcoal);
    box-shadow: 0 2px 6px rgba(0,0,0,0.35);
  }
  .card--front { left: 149px; }
  .card--back { left: 608px; }
  .card__shape { position: absolute; inset: 0; width: 100%; height: 100%; }

  .brand {
    position: absolute;
    top: 80px;
    width: 200px;
    text-align: center;
    color: var(--logo-silver);
    font-family: "Crimson Text", Georgia, serif;
    font-weight: 400;
    text-transform: uppercase;
  }
  .card--front .brand { left: 19px; }
  .card--back .brand { left: 24px; }
  .brand__mark {
    width: 72px; height: 72px;
    margin: 0 auto 10px;
    border-radius: 50%;
    background: var(--logo-silver);
  }
  .brand__name { white-space: nowrap; }
  .brand__line { display: block; }
  .brand__line--top { font-size: 15px; line-height: 16px; letter-spacing: 1.9px; }
  .brand__line--bottom { font-size: 21px; line-height: 19px; letter-spacing: 2.4px; }

  .contact {
    position: absolute;
    left: 244px;
    top: 72px;
    color: var(--text-white);
    font-size: 12px;
    line-height: 15px;
    white-space: nowrap;
  }
  .contact__name { font-size: 14px; font-weight: 600; color: var(--name-grey); line-height: 17px; }
  .contact__role { margin-bottom: 12px; }
  .contact__address { margin-bottom: 12px; }
  .contact__list { list-style: none; }
  .contact__list li { display: flex; align-items: center; height: 16px; }
  .contact__list svg { width: 9px; height: 9px; margin-right: 6px; fill: var(--text-white); }

  .services {
    position: absolute;
    left: 266px;
    top: 84px;
    list-style: none;
    color: var(--text-white);
    font-size: 12px;
    font-weight: 600;
  }
  .services li { display: flex; align-items: center; height: 23px; }
  .services li::before {
    content: "";
    width: 11px; height: 9px;
    border-radius: 50%;
    background: var(--logo-silver);
    margin-right: 10px;
  }
</style>
</head>
<body>

<section class="card card--front" aria-label="Card front">
  <svg class="card__shape" viewBox="0 0 440 271" aria-hidden="true">
    <path d="M228 0 C150 0 155 60 180 125 C202 182 240 228 252 271 L440 271 L440 0 Z" fill="var(--card-black)"/>
    <path d="M228 0 C150 0 155 60 180 125 C202 182 240 228 252 271" fill="none" stroke="var(--divider-white)" stroke-width="3"/>
  </svg>
  <div class="brand">
    <div class="brand__mark"></div>
    <p class="brand__name"><span class="brand__line brand__line--top">Helen Fosbury</span><span class="brand__line brand__line--bottom">Aesthetics</span></p>
  </div>
  <div class="contact">
    <p class="contact__name">Marcus Hale</p>
    <p class="contact__role">Managing Director</p>
    <p class="contact__address">52 Harwell Lane,<br>4 Brimfold High Street, TN7 4QW</p>
    <ul class="contact__list">
      <li><svg viewBox="0 0 10 10"><path d="M1 3 Q5 0 9 3 L8 4 L6.5 3.5 L6.5 2.5 Q5 2 3.5 2.5 L3.5 3.5 L2 4 Z M2 5 H8 V9 H2 Z"/></svg>0207 948 2176</li>
      <li><svg viewBox="0 0 10 10"><path d="M0 2 H10 V8 H0 Z M0.5 2.5 L5 6 L9.5 2.5" stroke="#000" stroke-width="0.8"/></svg>info@webname.com</li>
      <li><svg viewBox="0 0 10 10"><path d="M2 8 L4 6 M6 4 L8 2 M3 5 L5 7 M5 3 L7 5" stroke="#fff" stroke-width="1.4" fill="none"/></svg>www.websitename.com</li>
    </ul>
  </div>
</section>

<section class="card card--back" aria-label="Card back">
  <svg class="card__shape" viewBox="0 0 440 271" aria-hidden="true">
    <path d="M200 0 C170 0 175 50 195 110 C215 170 255 225 275 271 L440 271 L440 0 Z" fill="var(--card-black)"/>
    <path d="M200 0 C170 0 175 50 195 110 C215 170 255 225 275 271" fill="none" stroke="var(--divider-white)" stroke-width="3"/>
  </svg>
  <div class="brand">
    <div class="brand__mark"></div>
    <p class="brand__name"><span class="brand__line brand__line--top">Helen Fosbury</span><span class="brand__line brand__line--bottom">Aesthetics</span></p>
  </div>
  <ul class="services">
    <li>Velumin</li>
    <li>Lip Enhancement</li>
    <li>Chemical Peels</li>
    <li>Facial Fillers</li>
    <li>Non Surgical Face Lift</li>
  </ul>
</section>

</body>
</html>
```